Business Card for Voltrix

Horizontal business card for voltrix, the electrical contractor.
clean and professional looking, using company branding and colours.
I also want the blue in the logo and wording to be made a more 'electric' blue and the grey 'Voltrix' to be slightly darker.

Pleas use the following contact details:

Colin Marsh
Owner

t: 01736 582910
m: 07831 206719
e: colin@voltrix-installs.co.uk

www.voltrix-installs.co.uk

Industry/Entity Type

Electrical

Font styles to use
Sans Serif

```html
<!DOCTYPE html>
<html lang="en">
<head>
<meta charset="utf-8">
<title>Voltrix business card – front and back</title>
<link rel="stylesheet" href="https://fonts.googleapis.com/css2?family=Arimo:wght@400;700&family=Open+Sans:wght@400&display=swap">
<style>
  :root {
    --canvas: #ffffff;
    --charcoal: #4d4d4d;
    --teal: #9bcfcc;
    --teal-deep: #8ec6c4;
    --teal-light: #e9f4f3;
    --brand-grey: #7a8184;
    --ink: #ffffff;
    --label: #111111;
  }
  * { box-sizing: border-box; margin: 0; padding: 0; }
  html, body {
    width: 1200px; height: 1000px; overflow: hidden;
    background: var(--canvas);
    font-family: "Arimo", Arial, sans-serif;
  }
  .stage { position: relative; width: 1200px; height: 1000px; }

  .side-label {
    position: absolute; left: 54px;
    font-family: "Open Sans", sans-serif; font-size: 44px; color: var(--label);
  }
  .side-label--front { top: 238px; }
  .side-label--back { top: 695px; }

  .card {
    position: absolute; overflow: hidden;
    box-shadow: 2px 3px 5px rgba(0,0,0,0.35);
  }
  .card--front { left: 211px; top: 8px; width: 835px; height: 478px; background: #fff; }
  .card--back { left: 210px; top: 502px; width: 840px; height: 476px; }

  .card__waves { position: absolute; inset: 0; }

  .holder { position: absolute; left: 66px; top: 60px; width: 230px; text-align: center; color: var(--ink); }
  .holder__name { font-size: 31px; font-weight: 700; line-height: 1.1; }
  .holder__role { font-size: 24px; margin-top: 6px; }

  .contact { position: absolute; right: 56px; top: 48px; text-align: right; color: var(--ink); font-size: 24px; line-height: 32px; }
  .contact__web { margin-top: 32px; }

  .brand { position: absolute; display: flex; align-items: center; gap: 16px; }
  .brand__dot { width: 60px; height: 60px; border-radius: 50%; background: var(--teal); flex: none; }
  .brand__name { font-size: 64px; font-weight: 400; letter-spacing: 10px; color: var(--brand-grey); line-height: 1; }
  .card--front .brand { left: 56px; top: 348px; }

  .back-field {
    position: absolute; inset: 0;
    background: radial-gradient(ellipse at 50% 45%, var(--teal-light) 0%, var(--teal) 75%, var(--teal-deep) 100%);
  }
  .back-panel {
    position: absolute; left: 61px; top: 152px; width: 718px; height: 172px;
    background: #fff; border-radius: 12px;
    box-shadow: 0 6px 14px rgba(0,0,0,0.18);
    display: flex; align-items: center; justify-content: center;
  }
  .back-panel .brand { position: static; }
  .back-panel .brand__name { font-size: 58px; }
  .back-panel .brand__dot { width: 54px; height: 54px; }
</style>
</head>
<body>
<main class="stage">
  <p class="side-label side-label--front">front</p>
  <p class="side-label side-label--back">back</p>

  <section class="card card--front" aria-label="Card front">
    <svg class="card__waves" viewBox="0 0 835 478" width="835" height="478" aria-hidden="true">
      <path fill="var(--teal)" d="M0 206 C120 200 260 212 400 242 C600 286 740 372 835 352 V478 H712 C700 380 600 300 400 262 C250 234 110 222 0 222 Z"/>
      <path fill="var(--charcoal)" d="M0 0 H835 V368 C822 398 800 424 772 422 C716 418 690 330 560 282 C470 248 300 214 0 210 Z"/>
    </svg>
    <div class="holder">
      <p class="holder__name">Colin Marsh</p>
      <p class="holder__role">Owner</p>
    </div>
    <div class="contact">
      <p>t: 01736 582910</p>
      <p>m: 07831 206719</p>
      <p>e: colin@voltrix-installs.co.uk</p>
      <p class="contact__web">www.voltrix-installs.co.uk</p>
    </div>
    <div class="brand">
      <span class="brand__dot"></span>
      <span class="brand__name">VOLTRIX</span>
    </div>
  </section>

  <section class="card card--back" aria-label="Card back">
    <div class="back-field" role="img" aria-label="Teal background with a faint repeating brand pattern"></div>
    <div class="back-panel">
      <div class="brand">
        <span class="brand__dot"></span>
        <span class="brand__name">VOLTRIX</span>
      </div>
    </div>
  </section>
</main>
</body>
</html>
```